Southern Harvest Co, Seafood and Fresh Produce Website

Our organization is looking to design a simple, but eye catching website to show our services.
Our company exports West Australian FRESH fruit and vegetables, seafood and meat.
The website we are looking for would consist of:
- Landing Page
- Company info
- Directors bio
- Page that highlights our products
- Contact us page
We would like it to have a Chinese translated version as well.
Tobin
Target Market(s)
Chinese Market
Industry/Entity Type
It Company
Number of Pages Required
1 page
Look and feel
Each slider illustrates characteristics of the customer's brand and the style your logo design should communicate.

```html
<!DOCTYPE html>
<html lang="en">
<head>
<meta charset="utf-8">
<title>Southern Harvest Co</title>
<link href="https://fonts.googleapis.com/css2?family=Open+Sans:ital,wght@0,400;0,600;0,700;1,400&family=Oswald:wght@600&display=swap" rel="stylesheet">
<style>
  :root {
    --orange: #e8541d;
    --orange-dark: #c9410f;
    --orange-light: #f06a2a;
    --green: #6f9b1d;
    --green-footer: #7aa23a;
    --ink: #222222;
    --text: #333333;
    --muted: #666666;
    --band: #f0f0f0;
    --white: #ffffff;
  }
  * { margin: 0; padding: 0; box-sizing: border-box; }
  html, body { width: 721px; height: 1200px; overflow: hidden; }
  body {
    position: relative;
    background: linear-gradient(#e4e4e4 0, #ffffff 90px, #ffffff 100%);
    font-family: "Open Sans", Arial, sans-serif;
    color: var(--text);
  }
  .abs { position: absolute; }

  /* header */
  .brand-mark { left: 340px; top: 14px; width: 42px; height: 42px; border-radius: 50%; background: var(--green); }
  .brand-name { left: 0; width: 721px; top: 70px; text-align: center; font-weight: 700; font-size: 13px; color: var(--ink); }

  .main-nav { left: 92px; top: 97px; width: 537px; height: 28px;
    background: linear-gradient(var(--orange-light), var(--orange)); display: flex; }
  .main-nav a { color: var(--white); text-decoration: none; font-size: 10px; line-height: 28px; white-space: nowrap;
    text-align: center; border-right: 1px solid rgba(255,255,255,.25); }
  .main-nav a.active { background: var(--orange-dark); }
  .nav-phone { position: absolute; right: 8px; top: 0; height: 28px; display: flex; align-items: center; gap: 5px;
    font-family: "Oswald", sans-serif; font-weight: 600; font-size: 15px; color: var(--white); white-space: nowrap; }

  /* slider */
  .hero { left: 92px; top: 125px; width: 537px; height: 224px;
    background: radial-gradient(ellipse at 50% 45%, #9c2530 0, #6a1a22 35%, #3a2a22 70%, #5a4a40 100%); }
  .hero-caption { left: 92px; top: 322px; width: 537px; height: 24px; background: rgba(0,0,0,.45);
    color: var(--white); font-size: 11.5px; line-height: 24px; padding-left: 7px; }
  .hero-dots { left: 584px; top: 331px; display: flex; gap: 4px; }
  .hero-dots span { width: 6px; height: 6px; border-radius: 50%; background: #999; }
  .hero-dots span.on { background: var(--white); }

  /* welcome */
  .welcome-title { left: 0; width: 721px; top: 370px; text-align: center; font-size: 17px; font-weight: 400; color: var(--ink); }
  .welcome-text { left: 150px; width: 421px; top: 394px; text-align: center; font-size: 8px; line-height: 12.5px; color: var(--text); }
  .btn { display: block; background: var(--green); color: var(--white); font-size: 8.5px; text-align: center;
    border-radius: 10px; height: 20px; line-height: 20px; text-decoration: none; }

  /* products */
  .products { left: 0; top: 497px; width: 721px; height: 213px; background: var(--band); }
  .products-title { left: 0; width: 721px; top: 518px; text-align: center; font-size: 15px; font-weight: 400; color: var(--ink); }
  .product { top: 546px; width: 110px; text-align: center; }
  .product-photo { width: 110px; height: 110px; border-radius: 50%; border: 3px solid var(--white); }
  .product-name { margin-top: 10px; font-size: 10.5px; color: var(--ink); }
  .product-name.current { color: var(--orange); }

  /* about & services */
  .section-title { top: 736px; font-size: 14px; font-weight: 400; color: var(--ink); }
  .director-photo { left: 101px; top: 760px; width: 164px; height: 80px;
    background: linear-gradient(135deg, #8a8e92, #3c3f44 60%, #6a6e73); }
  .director-name { left: 272px; top: 758px; font-weight: 700; font-size: 9px; color: var(--orange); }
  .director-role { left: 272px; top: 773px; font-style: italic; font-size: 7.5px; color: var(--ink); }
  .body-text { font-size: 7.5px; line-height: 11.5px; color: var(--text); }
  .service-list { left: 400px; top: 848px; width: 220px; list-style: none; display: grid;
    grid-template-columns: 117px 103px; row-gap: 9px; }
  .service-list li { font-size: 7.5px; color: var(--ink); position: relative; padding-left: 10px;
    border-bottom: 1px solid #dddddd; padding-bottom: 5px; white-space: nowrap; }
  .service-list li::before { content: ""; position: absolute; left: 0; top: 3px; width: 4px; height: 4px;
    border-radius: 50%; background: var(--orange); }
  .service-list li.current { color: var(--orange); }
  .service-list li.current::before { background: #999; }

  /* contact */
  .map { left: 0; top: 966px; width: 721px; height: 198px;
    background: linear-gradient(90deg, #e2ddd2 0, #e9e6de 40%, #ece9e2 75%, #a9c5df 88%, #b5cde3 100%); }
  .quick-contact { left: 275px; top: 988px; width: 173px; height: 158px; background: rgba(80,80,80,.75); border-radius: 4px; }
  .quick-title { left: 275px; width: 173px; top: 998px; text-align: center; color: var(--white); font-size: 11px; letter-spacing: .5px; }
  .field { left: 284px; width: 153px; background: var(--white); font-size: 7px; color: #999; padding: 4px 5px; }
  .submit { left: 333px; top: 1110px; width: 56px; height: 18px; line-height: 18px; border-radius: 9px;
    background: var(--orange); color: var(--white); font-size: 7.5px; text-align: center; }

  /* footer */
  .footer { left: 0; top: 1164px; width: 721px; height: 36px; background: var(--green-footer); }
  .footer-note { left: 101px; top: 1177px; font-size: 7.5px; color: var(--ink); }
  .footer-note b { font-weight: 700; }
  .social { left: 557px; top: 1175px; display: flex; gap: 5px; }
  .social span { width: 14px; height: 14px; border-radius: 50%; background: #b6cf8a; }
</style>
</head>
<body>

<header>
  <div class="abs brand-mark"></div>
  <div class="abs brand-name">SOUTHERN HARVEST CO</div>
  <nav class="abs main-nav">
    <a class="active" href="#" style="width:63px;">HOME</a>
    <a href="#" style="width:82px;">ABOUT US</a>
    <a href="#" style="width:83px;">PRODUCTS</a>
    <a href="#" style="width:70px;">NEWS</a>
    <a href="#" style="width:90px;">CONTACT US</a>
    <div class="nav-phone">
      <svg width="13" height="13" viewBox="0 0 14 14"><circle cx="7" cy="7" r="6.3" fill="none" stroke="#5a1e08" stroke-width="1.2"/><path d="M4.5 4c.6-.5 1-.4 1.3.2l.5 1c.2.4 0 .7-.3.9-.2.2-.2.5 0 .9.4.6.8 1 1.4 1.4.4.2.7.2.9 0 .2-.3.5-.5.9-.3l1 .5c.6.3.7.7.2 1.3-.7.8-1.8.8-3 0C6.1 9.1 5 8 4.3 6.8c-.6-1.1-.5-2.1.2-2.8z" fill="#5a1e08"/></svg>
      555-014-2290
    </div>
  </nav>
</header>

<section class="slider">
  <div class="abs hero" role="img" aria-label="Raw seasoned beef steak with rosemary and peppercorns on a wooden board"></div>
  <div class="abs hero-caption">COMMITTED TO HIGH QUALITY AND EXCELLENCE</div>
  <div class="abs hero-dots"><span class="on"></span><span></span><span></span><span></span><span></span></div>
</section>

<section class="welcome">
  <h1 class="abs welcome-title">Welcome to Southern Harvest Co</h1>
  <p class="abs welcome-text">We export fresh produce, seafood and premium meat from the west coast to kitchens and markets across Asia. Every shipment is picked, packed and chilled with care, so it arrives in the same condition it left the farm.</p>
  <a class="abs btn" href="#" style="left:325px; top:440px; width:70px;">READ MORE</a>
</section>

<section>
  <div class="abs products"></div>
  <h2 class="abs products-title">Our Products</h2>
  <div class="abs product" style="left:111px;">
    <div class="product-photo" role="img" aria-label="Fresh vegetables including broccoli, tomatoes and greens" style="background:radial-gradient(circle,#6f9a3a,#3d6a22 60%,#b8322a)"></div>
    <div class="product-name">VEGETABLES</div>
  </div>
  <div class="abs product" style="left:243px;">
    <div class="product-photo" role="img" aria-label="Fresh fruit including grapefruit, lemons and apples" style="background:radial-gradient(circle,#f2b33a,#e0602a 55%,#c8262a)"></div>
    <div class="product-name">FRUITS</div>
  </div>
  <div class="abs product" style="left:375px;">
    <div class="product-photo" role="img" aria-label="Cuts of raw meat with garlic, in greyscale" style="background:radial-gradient(circle,#bdbdbd,#7e7e7e 60%,#4a4a4a)"></div>
    <div class="product-name current">MEAT</div>
  </div>
  <div class="abs product" style="left:507px;">
    <div class="product-photo" role="img" aria-label="Whole red fish served with green beans" style="background:radial-gradient(circle,#b0562e,#6a3a1e 55%,#3c4a2a)"></div>
    <div class="product-name">SEA FOOD</div>
  </div>
</section>

<section class="about">
  <h2 class="abs section-title" style="left:101px;">About Us</h2>
  <div class="abs director-photo" role="img" aria-label="Portrait of the company director in a suit"></div>
  <div class="abs director-name">Dr. Jared Tobin</div>
  <div class="abs director-role">Director</div>
  <p class="abs body-text" style="left:272px; top:786px; width:112px;">Jared has spent twenty years building supply links with farmers and fishers across the region.</p>
  <p class="abs body-text" style="left:101px; top:843px; width:281px;">We work directly with growers and processors across the region, checking every batch before it leaves the port. Our team handles packing, cold storage, paperwork and shipping, so our partners receive reliable supply all year round with no surprises along the way.</p>
  <a class="abs btn" href="#" style="left:101px; top:916px; width:66px; height:18px; line-height:18px;">READ MORE</a>
</section>

<section class="services">
  <h2 class="abs section-title" style="left:398px;">Our Services</h2>
  <p class="abs body-text" style="left:400px; top:759px; width:222px;">We offer sourcing, grading, cold chain logistics and export documentation for fresh goods. Our staff speak English and Mandarin and guide each client from first enquiry to final delivery, with clear pricing and regular updates at every step of the journey.</p>
  <ul class="abs service-list">
    <li>FRESH PRODUCE SOURCING</li>
    <li>COLD CHAIN SHIPPING</li>
    <li class="current">EXPORT PAPERWORK</li>
    <li>QUALITY GRADING</li>
    <li>MARKET RESEARCH</li>
    <li>CUSTOM PACKING</li>
  </ul>
  <a class="abs btn" href="#" style="left:400px; top:916px; width:64px; height:18px; line-height:18px;">READ MORE</a>
</section>

<section class="contact">
  <div class="abs map" role="img" aria-label="Street map of the city centre and harbour"></div>
  <div class="abs quick-contact"></div>
  <div class="abs quick-title">QUICK CONTACT</div>
  <div class="abs field" style="top:1019px; height:15px;">Name</div>
  <div class="abs field" style="top:1041px; height:15px;">E-mail</div>
  <div class="abs field" style="top:1063px; height:38px;">Message</div>
  <div class="abs submit">SUBMIT</div>
</section>

<footer>
  <div class="abs footer"></div>
  <div class="abs footer-note">© 2015. <b>Southern Harvest Co.</b> All rights reserved.</div>
  <div class="abs social"><span></span><span></span><span></span><span></span></div>
</footer>

</body>
</html>
```